International Trading Company, 'KIRO' needs a Business Card

The company name is "KIRO" and it has own logo design.
I'd like to use its logo on this business card.
I need two side Business Card.
I'll look forward to your great design.
Thank you very much in advance.

Contact Information for Business Card

Company Name : Kiro Harbour Limited
Information Example
Dorian Pallister
Mobile(use icon please) : 1 (212) 555-0143
Tel(use icon please) : 1 (212) 555-0178
Email(use icon please) : dorian27@kiroharbour-mail.com
Address(use icon please) : 482 Halden Ave, New York, NY 10160, USA

```html
<!DOCTYPE html>
<html lang="en">
<head>
<meta charset="UTF-8">
<title>Kiro Harbour Limited — Business Card</title>
<link href="https://fonts.googleapis.com/css2?family=Michroma&family=Lato:wght@400&display=swap" rel="stylesheet">
<style>
  :root {
    --stage: #1b1b1b;
    --card: #121212;
    --card-edge: #0c0c0c;
    --pattern-a: #161616;
    --pattern-b: #101010;
    --logo-front: #b9b9b9;
    --logo-back: #7c7c7c;
    --name: #9c9c9c;
    --role: #6c6c6c;
    --rule: #4a4a4a;
    --contact: #8e8e8e;
    --icon: #6e6e6e;
  }
  * { box-sizing: border-box; margin: 0; padding: 0; }
  html, body { width: 1200px; height: 1200px; overflow: hidden; }
  body { background: var(--stage); position: relative; font-family: "Lato", sans-serif; }

  .card {
    position: absolute;
    left: 160px;
    width: 880px;
    height: 503px;
    background: var(--card);
    border: 1px solid var(--card-edge);
    box-shadow: 0 18px 40px rgba(0,0,0,0.55);
    overflow: hidden;
  }
  .card--front { top: 72px; }
  .card--back { top: 625px; }

  .front-pattern {
    position: absolute; inset: 0;
    background: linear-gradient(135deg, var(--pattern-a), var(--pattern-b));
  }
  .front-logo {
    position: absolute;
    left: 80px; top: 250px;
    font-family: "Michroma", sans-serif;
    font-size: 96px;
    letter-spacing: 2px;
    color: var(--logo-front);
    line-height: 1;
  }

  .brand { position: absolute; right: 70px; top: 48px; text-align: right; }
  .brand__mark {
    font-family: "Michroma", sans-serif;
    font-size: 112px; line-height: 1;
    color: var(--logo-back);
  }
  .brand__name {
    font-family: "Michroma", sans-serif;
    font-size: 25px; letter-spacing: 4px;
    color: var(--logo-back);
    margin-top: 6px;
  }

  .person { position: absolute; left: 70px; top: 215px; }
  .person__name {
    font-family: "Michroma", sans-serif;
    font-size: 24px; letter-spacing: 5px;
    color: var(--name);
  }
  .person__role {
    font-family: "Michroma", sans-serif;
    font-size: 20px; letter-spacing: 5px;
    color: var(--role);
    margin-top: 4px;
  }
  .rule {
    position: absolute; left: 70px; right: 70px; top: 300px;
    height: 1px; background: var(--rule);
  }

  .contacts { position: absolute; left: 70px; top: 322px; list-style: none; }
  .contacts li {
    display: flex; align-items: center; gap: 16px;
    font-size: 24px; color: var(--contact);
    height: 38px;
  }
  .contacts svg, .address svg { fill: var(--icon); flex: none; }

  .address {
    position: absolute; right: 70px; top: 340px;
    display: flex; align-items: center; gap: 18px;
    text-align: right; font-size: 24px; line-height: 1.45;
    color: var(--contact);
  }
</style>
</head>
<body>
  <section class="card card--front" aria-label="Card front">
    <div class="front-pattern" role="img" aria-label="Faint repeating company-name texture across the card"></div>
    <div class="front-logo">KIRO</div>
  </section>

  <section class="card card--back" aria-label="Card back">
    <div class="brand">
      <div class="brand__mark">KIRO</div>
      <div class="brand__name">KIRO HARBOUR LIMITED</div>
    </div>

    <div class="person">
      <div class="person__name">DORIAN PALLISTER</div>
      <div class="person__role">OWNER</div>
    </div>

    <div class="rule"></div>

    <ul class="contacts">
      <li>
        <svg width="18" height="24" viewBox="0 0 18 24" aria-hidden="true"><path d="M3 0h12a2 2 0 0 1 2 2v20a2 2 0 0 1-2 2H3a2 2 0 0 1-2-2V2a2 2 0 0 1 2-2zm0 3v15h12V3zm6 17a1.3 1.3 0 1 0 0 2.6A1.3 1.3 0 0 0 9 20z"/></svg>
        1 (212) 555-0143
      </li>
      <li>
        <svg width="24" height="20" viewBox="0 0 24 20" aria-hidden="true"><path d="M2 5c3-4 17-4 20 0l-1 3-5-1-1-2H9L8 7 3 8zM6 9h12l3 9H3zm6 2a3 3 0 1 0 0 6 3 3 0 0 0 0-6z"/></svg>
        1 (212) 555-0178
      </li>
      <li>
        <svg width="24" height="18" viewBox="0 0 24 18" aria-hidden="true"><path d="M0 0h24v18H0zm2 2v.6l10 7 10-7V2zm0 3v11h20V5l-10 7z"/></svg>
        dorian27@kiroharbour-mail.com
      </li>
    </ul>

    <div class="address">
      <div>482 Halden Ave, New York<br>NY 10160, USA</div>
      <svg width="20" height="28" viewBox="0 0 20 28" aria-hidden="true"><path d="M10 0a10 10 0 0 1 10 10c0 7-10 18-10 18S0 17 0 10A10 10 0 0 1 10 0zm0 6a4 4 0 1 0 0 8 4 4 0 0 0 0-8z"/></svg>
    </div>
  </section>
</body>
</html>
```